New website design for small car detailing company.

We have a small cleaning company, our main focus is car detailing but we are also expanding to home and residential cleaning and power washing.
I would like the web site to have a simple layout and SEO friendly.
I would also like to have a contact page in which clients can contact us and upload pictures of the house or car so we can provide an estimate.
A Page that shows the services we offer.

Target Market(s)

High paying clients for car detailiing and focus on residential and commercial cleaning.

Industry/Entity Type

Cleaning Service

Coding

Coded - Design and coding required

Number of Pages Required

4 page

Font styles to use
Serif

Colors

Designer to choose only greyscale colors for use in the design.

Requirements
Must have
• A home page.
Blog page for SEO
Contact page with the choice of clients to upload theirs pictures so we can provide estimates with calendar integration so they can provide their available dates for service.
A pictures to sell our services.
Nice to have
• Simple but sleek desing, I am more interested in SEO Score than heavy loads

```html
<!DOCTYPE html>
<html lang="en">
<head>
<meta charset="utf-8">
<title>Harbor Point Mobile Detailing</title>
<link rel="stylesheet" href="https://fonts.googleapis.com/css2?family=Oswald:wght@500;600&family=Mulish:wght@400;600;700&display=swap">
<style>
:root{
  --ink:#1d1d1d;
  --text:#3a3a3a;
  --muted:#8a8a8a;
  --accent:#e8551f;
  --paper:#ffffff;
  --band:#f4f4f4;
  --foot:#f3f4f7;
  --line:#d6d6d6;
}
*{margin:0;padding:0;box-sizing:border-box}
html,body{width:1200px;height:3865px;overflow:hidden}
body{position:relative;background:var(--paper);font-family:'Mulish',sans-serif;color:var(--text)}
.abs{position:absolute}
.head{font-family:'Oswald',sans-serif;font-weight:600;color:var(--ink);text-transform:uppercase;letter-spacing:-.3px}
.btn{position:absolute;display:flex;align-items:center;justify-content:center;font-family:'Oswald',sans-serif;font-weight:500;text-transform:uppercase;color:#fff;font-size:16px;border-radius:3px}
.btn-accent{background:var(--accent)}
.btn-dark{background:var(--ink)}

/* hero */
.hero-photo{left:0;top:0;width:1200px;height:640px;clip-path:polygon(0 0,100% 0,100% 522px,600px 640px,0 562px);
  background:linear-gradient(100deg,#e9e6e2 0%,#dcd6cf 30%,#c9a68c 55%,#b98a6e 75%,#8f9db3 100%)}
.hero-edge{left:0;top:0}
.brand{left:132px;top:40px;width:160px;display:flex;flex-direction:column;align-items:center;gap:10px}
.brand-mark{width:70px;height:70px;border-radius:50%;background:var(--ink)}
.brand-name{font-family:'Mulish',sans-serif;font-weight:700;font-size:15px;line-height:19px;color:var(--ink);text-align:center;text-transform:uppercase}
.nav{top:36px;left:405px;display:flex;gap:35px;font-family:'Oswald',sans-serif;font-size:16px;color:var(--ink);text-transform:uppercase}
.call-top{left:912px;top:26px;display:flex;gap:12px;align-items:center}
.call-top small{display:block;font-size:11px;text-transform:uppercase;color:var(--ink);font-weight:700}
.call-top b{font-family:'Oswald',sans-serif;font-size:25px;font-weight:600;color:var(--ink);line-height:28px}
.hero-kicker{left:133px;top:266px;font-family:'Oswald',sans-serif;font-size:21px;color:var(--ink);text-transform:uppercase;font-weight:500}
.hero-title{left:133px;top:296px;font-size:39px;line-height:50px}

/* about */
.centered{left:0;width:1200px;text-align:center}
.section-title{font-size:45px;line-height:55px}
.about-sub{top:777px;font-size:18px;font-weight:600;color:var(--ink)}
.about-copy{left:158px;width:884px;text-align:center;font-size:14px;line-height:26px;color:var(--text)}

/* services */
.services-band{left:0;top:1132px;width:1200px;height:641px;background:var(--band)}
.card{position:absolute;top:1292px;width:219px;height:328px;background:#fff;box-shadow:0 2px 8px rgba(0,0,0,.06);overflow:hidden;text-align:center}
.card-photo{position:absolute;left:0;top:0;width:219px;height:150px}
.card-curve{position:absolute;left:0;top:100px}
.card-icon{position:absolute;left:80px;top:118px;width:58px;height:58px;border-radius:50%;background:#fff;display:flex;align-items:center;justify-content:center}
.card h3{position:absolute;top:180px;width:100%;font-size:17px}
.card p{position:absolute;top:210px;left:14px;width:191px;font-size:12px;line-height:20px}
.card .more{position:absolute;top:290px;width:100%;font-size:11px;font-weight:700;color:var(--ink)}

/* trust */
.trust-item{position:absolute;width:260px}
.trust-item h4{font-size:18px;font-weight:600;color:var(--ink);line-height:22px}
.trust-item p{font-size:13px;line-height:17px;color:var(--muted);margin-top:2px}
.left-item{text-align:right}
.ring{position:absolute;border-radius:50%;background:#fff;box-shadow:0 2px 10px rgba(0,0,0,.12);display:flex;align-items:center;justify-content:center}
.center-badge{left:423px;top:1953px;width:354px;height:354px;border-radius:50%;background:#fff;box-shadow:0 4px 24px rgba(0,0,0,.1);display:flex;flex-direction:column;align-items:center;justify-content:center;gap:14px}

/* cta */
.cta-dark{left:0;top:2394px;width:600px;height:432px;background:#232222}
.cta-photo{left:600px;top:2394px;width:600px;height:432px;background:linear-gradient(120deg,#f1f1ef 0%,#d7dde6 40%,#6f8fc2 60%,#e6d8a6 80%,#f4f4f2 100%)}
.cta-title{left:133px;top:2456px;font-size:54px;line-height:56px;color:#fff}

/* blog */
.post{position:absolute;top:2982px;width:299px;height:378px;background:#fff;box-shadow:0 3px 12px rgba(0,0,0,.08)}
.post-photo{width:299px;height:183px}
.post-date{position:absolute;top:192px;left:17px;font-size:13px;color:var(--text);display:flex;gap:8px;align-items:center}
.post h3{position:absolute;top:224px;left:17px;width:270px;font-size:19px;line-height:25px}
.post p{position:absolute;top:285px;left:17px;width:270px;font-size:13px;line-height:21px}
.post a{position:absolute;top:338px;left:17px;font-size:13px;color:var(--accent);text-decoration:underline;font-weight:600}

/* footer */
.foot-bg{left:0;top:3475px;width:1200px;height:390px;background:var(--foot);clip-path:polygon(0 80px,600px 0,1200px 80px,1200px 100%,0 100%)}
.foot-nav{top:3572px;left:370px;display:flex;align-items:center;font-size:16px;font-weight:600;color:var(--ink)}
.foot-nav span.sep{width:1px;height:20px;background:var(--line);margin:0 42px}
.contact-block{position:absolute;display:flex;gap:16px;align-items:flex-start;font-size:14px;line-height:23px;color:var(--text)}
.contact-block strong{display:block;font-weight:600;color:var(--ink);text-transform:uppercase;font-size:14px}
.dot{width:40px;height:40px;border-radius:50%;background:var(--ink);display:flex;align-items:center;justify-content:center;flex:none}
.copy{left:133px;top:3813px;font-size:14px;color:var(--text)}
.social{position:absolute;top:3807px;width:30px;height:30px;border-radius:50%;border:1.5px solid var(--ink)}
</style>
</head>
<body>

<!-- hero -->
<div class="abs hero-photo" role="img" aria-label="Smiling family of four relaxing together on a sofa"></div>
<svg class="abs hero-edge" width="1200" height="645" viewBox="0 0 1200 645"><polyline points="0,562 600,640 1200,522" fill="none" stroke="#1d1d1d" stroke-width="3"/></svg>

<div class="abs brand"><div class="brand-mark"></div><div class="brand-name">Harbor Point Mobile Detailing</div></div>
<nav class="abs nav"><span>Home</span><span>Services</span><span>Blog</span><span>Contact</span></nav>
<div class="btn btn-accent" style="left:725px;top:27px;width:167px;height:40px">Request an Estimate</div>
<div class="abs call-top">
  <svg width="18" height="32" viewBox="0 0 18 32"><rect x="1" y="1" width="16" height="30" rx="3" fill="none" stroke="#1d1d1d" stroke-width="2.5"/><rect x="6" y="25" width="6" height="2" fill="#1d1d1d"/></svg>
  <div><small>Call us today!</small><b>012-555-0148</b></div>
</div>

<div class="abs hero-kicker">We provide car detailiing and also</div>
<h1 class="abs head hero-title">Expanding to residential,<br>commercial cleaning and<br>power washing</h1>
<div class="btn btn-accent" style="left:132px;top:457px;width:168px;height:38px">Request an Estimate</div>

<!-- about -->
<h2 class="abs head centered section-title" style="top:714px">About Harbor Point Mobile Detailing</h2>
<p class="abs centered about-sub">Exterior Cleaning To Make Your Life Easier</p>
<p class="abs about-copy" style="top:816px">Donec rutrum elit at velit feugiat, condimentum tincidunt ligula aliquet. Nullam et felis ut lectus ornare pellentesque eget at turpis. Sed ultrices ante ac sem porttitor, id lobortis augue ullamcorper. Vivamus nunc augue, molestie a diam elementum, aliquet molestie mattis lorem turpis, et fermentum enim rhoncus quis risus. Morbi fringilla metus tortor, et viverra elit iaculis ut.</p>
<p class="abs about-copy" style="top:904px">Nulla sagittis ut neque vitae pretium. Aliquam erat volutpat. Sied auctor magna lacus, id elementum nibh posuere vitae. Etiamlore quam, semper sed augue non, dignissim tristique sem. Classapte taciti sociosqu ad litora torquent per conubia nostra, per inceptos magna lacus, id elementum nibh Aliquam erat volutpat sied auctor magna lacus nisi quis lectus himenaeos.</p>
<div class="btn btn-accent" style="left:427px;top:1008px;width:167px;height:39px">Request an Estimate</div>
<div class="btn btn-dark" style="left:605px;top:1008px;width:168px;height:39px">Call (012) 555-0148</div>

<!-- services -->
<div class="abs services-band"></div>
<h2 class="abs head centered section-title" style="top:1202px">Our Services</h2>

<article class="card" style="left:132px">
  <div class="card-photo" role="img" aria-label="Detailer cleaning a car interior" style="background:linear-gradient(135deg,#2b2b2b,#7a7a7a 60%,#cfcfcf)"></div>
  <svg class="card-curve" width="219" height="60" viewBox="0 0 219 60"><path d="M0 0 Q109 75 219 0 V60 H0 Z" fill="#fff"/></svg>
  <div class="card-icon"><svg width="34" height="26" viewBox="0 0 34 26" fill="none" stroke="#1d1d1d" stroke-width="2"><path d="M4 14 L8 5 H26 L30 14 V21 H4 Z"/><circle cx="10" cy="16" r="2"/><circle cx="24" cy="16" r="2"/><path d="M6 21 V25 M28 21 V25"/></svg></div>
  <h3 class="head">Car Detailing</h3>
  <p>Lorem ipsum dolor sit amet consctetuer adipiscing elit, sed diiam nonummy nibh.</p>
  <div class="more">READ MORE →</div>
</article>
<article class="card" style="left:370px">
  <div class="card-photo" role="img" aria-label="Cleaner vacuuming a living room" style="background:linear-gradient(135deg,#e8e4de,#b8a28c 55%,#5b4538)"></div>
  <svg class="card-curve" width="219" height="60" viewBox="0 0 219 60"><path d="M0 0 Q109 75 219 0 V60 H0 Z" fill="#fff"/></svg>
  <div class="card-icon"><svg width="32" height="30" viewBox="0 0 32 30" fill="none" stroke="#1d1d1d" stroke-width="2"><path d="M3 14 L16 3 L29 14"/><path d="M7 11 V28 H25 V11"/><rect x="13" y="19" width="6" height="9"/></svg></div>
  <h3 class="head">Residential Cleaning</h3>
  <p>Lorem ipsum dolor sit amet consctetuer adipiscing elit, sed diiam nonummy nibh.</p>
  <div class="more">READ MORE →</div>
</article>
<article class="card" style="left:609px">
  <div class="card-photo" role="img" aria-label="Window cleaners on a glass office tower" style="background:linear-gradient(135deg,#5f86b8,#b9cde6 50%,#3c5f8e)"></div>
  <svg class="card-curve" width="219" height="60" viewBox="0 0 219 60"><path d="M0 0 Q109 75 219 0 V60 H0 Z" fill="#fff"/></svg>
  <div class="card-icon"><svg width="26" height="32" viewBox="0 0 26 32" fill="none" stroke="#1d1d1d" stroke-width="2"><rect x="5" y="2" width="16" height="28"/><path d="M9 7h2M15 7h2M9 13h2M15 13h2M9 19h2M15 19h2M11 30v-5h4v5M1 30h24"/></svg></div>
  <h3 class="head">Commercial Cleaning</h3>
  <p>Lorem ipsum dolor sit amet consctetuer adipiscing elit, sed diiam nonummy nibh.</p>
  <div class="more">READ MORE →</div>
</article>
<article class="card" style="left:848px">
  <div class="card-photo" role="img" aria-label="Worker power washing a deck" style="background:linear-gradient(135deg,#c08a52,#e3c79b 45%,#d0692f 70%,#6b5a4a)"></div>
  <svg class="card-curve" width="219" height="60" viewBox="0 0 219 60"><path d="M0 0 Q109 75 219 0 V60 H0 Z" fill="#fff"/></svg>
  <div class="card-icon"><svg width="28" height="32" viewBox="0 0 28 32" fill="none" stroke="#1d1d1d" stroke-width="2"><path d="M6 30 V12 L10 4 H13 V30 Z"/><path d="M20 30 V16 H25 V30 Z M22 16 V10"/></svg></div>
  <h3 class="head">Power Washing</h3>
  <p>Lorem ipsum dolor sit amet consctetuer adipiscing elit, sed diiam nonummy nibh.</p>
  <div class="more">READ MORE →</div>
</article>
<div class="btn btn-accent" style="left:514px;top:1660px;width:168px;height:39px">Request an Estimate</div>

<!-- why trust -->
<h2 class="abs head centered section-title" style="top:1849px">Why Trusts Harbor Point Mobile</h2>
<svg class="abs" style="left:0;top:1960px" width="1200" height="300" viewBox="0 0 1200 300" fill="none" stroke="#cfcfcf" stroke-width="2">
  <path d="M380 50 Q340 100 338 130"/><path d="M338 180 Q340 220 350 240"/>
  <path d="M822 50 Q860 100 862 130"/><path d="M862 180 Q860 220 850 240"/>
</svg>

<div class="trust-item left-item" style="left:80px;top:1956px"><h4>WOW Experience</h4><p>Duis autem vel eum iriure dolor in<br>hendrerit in vulputate</p></div>
<div class="ring" style="left:353px;top:1953px;width:72px;height:72px;background:var(--ink)"><svg width="34" height="34" viewBox="0 0 34 34" fill="none" stroke="#fff" stroke-width="2"><circle cx="17" cy="17" r="14"/><path d="M17 8 L19.5 14 H26 L21 18 L23 25 L17 21 L11 25 L13 18 L8 14 H14.5 Z"/></svg></div>

<div class="trust-item left-item" style="left:30px;top:2076px"><h4>Timeless Services</h4><p>Duis autem vel eum iriure dolork<br>in hendrerit in vulputate</p></div>
<div class="ring" style="left:303px;top:2073px;width:72px;height:72px"><svg width="36" height="36" viewBox="0 0 36 36" fill="none" stroke="#1d1d1d" stroke-width="2"><circle cx="18" cy="18" r="15"/><path d="M18 9 V18 L24 22"/></svg></div>

<div class="trust-item left-item" style="left:40px;top:2196px"><h4>Best Customer Support</h4><p>Duis autem vel eum iriure dolor in<br>hendrerit in vulputate</p></div>
<div class="ring" style="left:320px;top:2192px;width:72px;height:72px"><svg width="36" height="36" viewBox="0 0 36 36" fill="none" stroke="#1d1d1d" stroke-width="2"><circle cx="18" cy="18" r="15"/><text x="18" y="23" text-anchor="middle" font-family="Mulish,sans-serif" font-size="13" font-weight="700" fill="#1d1d1d" stroke="none">24</text></svg></div>

<div class="center-badge">
  <div class="brand-mark" style="width:96px;height:96px"></div>
  <div class="brand-name" style="font-size:20px;line-height:25px;width:220px">Harbor Point Mobile Detailing</div>
</div>
<div class="btn btn-dark" style="left:489px;top:2257px;width:222px;height:53px;font-size:22px">Call (012) 555-0148</div>

<div class="ring" style="left:779px;top:1953px;width:72px;height:72px"><svg width="36" height="36" viewBox="0 0 36 36" fill="none" stroke="#1d1d1d" stroke-width="2"><path d="M18 3 L22 7 L28 7 L29 13 L33 18 L29 23 L28 29 L22 29 L18 33 L14 29 L8 29 L7 23 L3 18 L7 13 L8 7 L14 7 Z"/><path d="M12 18 L16 22 L24 14"/></svg></div>
<div class="trust-item" style="left:863px;top:1956px"><h4>100% Satisfaction Guaranteed</h4><p>Duis autem vel eum iriure dolor in<br>hendrerit in vulputate</p></div>

<div class="ring" style="left:827px;top:2073px;width:72px;height:72px"><svg width="36" height="36" viewBox="0 0 36 36" fill="none" stroke="#1d1d1d" stroke-width="2"><path d="M10 32 V20 L8 12 M10 20 L14 8 M14 20 L18 6 M18 20 L22 8 M22 22 L28 16 M10 32 H22 L26 22"/><circle cx="28" cy="8" r="2"/></svg></div>
<div class="trust-item" style="left:913px;top:2076px"><h4>Attention To Detail</h4><p>Duis autem vel eum iriure dolormk<br>in hendrerit in vulputate</p></div>

<div class="ring" style="left:815px;top:2192px;width:72px;height:72px"><svg width="36" height="36" viewBox="0 0 36 36" fill="none" stroke="#1d1d1d" stroke-width="2"><circle cx="18" cy="14" r="10"/><circle cx="18" cy="14" r="5"/><path d="M12 22 L9 33 L14 30 L17 34 M24 22 L27 33 L22 30 L19 34"/></svg></div>
<div class="trust-item" style="left:902px;top:2196px"><h4>Licensed &amp; Insured</h4><p>Duis autem vel eum iriure dolor in<br>hendrerit in vulputate</p></div>

<!-- cta -->
<div class="abs cta-dark"></div>
<div class="abs cta-photo" role="img" aria-label="Technician shaking hands with a homeowner at her front door"></div>
<h2 class="abs head cta-title">Get your detailing<br>business to work<br>for you. Work less,<br>make more.</h2>
<div class="btn btn-accent" style="left:132px;top:2703px;width:201px;height:47px;font-size:19px">Request an Estimate</div>

<!-- blog -->
<h2 class="abs head centered section-title" style="top:2894px">Blog Posts</h2>
<svg class="abs" style="left:74px;top:3160px" width="28" height="20" viewBox="0 0 28 20" fill="none" stroke="#555" stroke-width="1.6"><path d="M26 10 H3 M10 3 L3 10 L10 17"/></svg>
<svg class="abs" style="left:1098px;top:3160px" width="28" height="20" viewBox="0 0 28 20" fill="none" stroke="#1d1d1d" stroke-width="1.6"><path d="M2 10 H25 M18 3 L25 10 L18 17"/></svg>

<article class="post" style="left:132px">
  <div class="post-photo" role="img" aria-label="Rope access worker cleaning a glass facade" style="background:linear-gradient(135deg,#4a5d78,#a9b9cf 55%,#6b7c93)"></div>
  <div class="post-date"><svg width="12" height="12" viewBox="0 0 12 12"><rect x="1" y="2" width="10" height="9" fill="none" stroke="#3a3a3a"/><rect x="1" y="2" width="10" height="3" fill="#3a3a3a"/></svg>28 AUG, 2020</div>
  <h3 class="head">Nulla sit amet lorem et est porttitor vestibulum eu at est.</h3>
  <p>In pulvinar turpis vel risus hendrerit, etlore porta turpis euismod.</p>
  <a>READ MORE</a>
</article>
<article class="post" style="left:450px">
  <div class="post-photo" role="img" aria-label="Crew cleaning a large empty warehouse floor" style="background:linear-gradient(160deg,#f2f2f0,#d6d6d2 55%,#b9b6ae)"></div>
  <div class="post-date"><svg width="12" height="12" viewBox="0 0 12 12"><rect x="1" y="2" width="10" height="9" fill="none" stroke="#3a3a3a"/><rect x="1" y="2" width="10" height="3" fill="#3a3a3a"/></svg>28 AUG, 2020</div>
  <h3 class="head">Nulla sit amet lorem et est porttitor vestibulum eu at est.</h3>
  <p>In pulvinar turpis vel risus hendrerit, etlore porta turpis euismod.</p>
  <a>READ MORE</a>
</article>
<article class="post" style="left:768px">
  <div class="post-photo" role="img" aria-label="Dark car being rinsed with a spray of water" style="background:linear-gradient(135deg,#1e1e1e,#6e6e6e 50%,#d8d8d8)"></div>
  <div class="post-date"><svg width="12" height="12" viewBox="0 0 12 12"><rect x="1" y="2" width="10" height="9" fill="none" stroke="#3a3a3a"/><rect x="1" y="2" width="10" height="3" fill="#3a3a3a"/></svg>28 AUG, 2020</div>
  <h3 class="head">Nulla sit amet lorem et est porttitor vestibulum eu at est.</h3>
  <p>In pulvinar turpis vel risus hendrerit, etlore porta turpis euismod.</p>
  <a>READ MORE</a>
</article>

<!-- footer -->
<div class="abs foot-bg"></div>
<svg class="abs" style="left:0;top:3470px" width="1200" height="90" viewBox="0 0 1200 90"><polyline points="0,85 600,5 1200,85" fill="none" stroke="#1d1d1d" stroke-width="3"/></svg>
<nav class="abs foot-nav"><span>Home</span><span class="sep"></span><span>Services</span><span class="sep"></span><span>Blog</span><span class="sep"></span><span>Contact</span></nav>

<div class="contact-block" style="left:132px;top:3670px">
  <div class="dot"><svg width="14" height="20" viewBox="0 0 14 20"><path d="M7 1 C3 1 1 4 1 7 C1 11 7 19 7 19 C7 19 13 11 13 7 C13 4 11 1 7 1 Z" fill="#fff"/><circle cx="7" cy="7" r="2.3" fill="#1d1d1d"/></svg></div>
  <div><strong>Harbor Point Mobile Detailing</strong>48 Quay Lane, Dockside Road<br>Bayfield, XY - 40721</div>
</div>
<div class="abs" style="left:495px;top:3666px;width:1px;height:70px;background:var(--line)"></div>
<div class="contact-block" style="left:540px;top:3682px">
  <div class="dot"><svg width="18" height="18" viewBox="0 0 18 18"><path d="M4 1 L7 5 L5 7 C6 10 8 12 11 13 L13 11 L17 14 L15 17 C8 17 1 10 1 3 Z" fill="#fff"/></svg></div>
  <div><strong>Phone</strong>012-555-0148</div>
</div>
<div class="abs" style="left:747px;top:3666px;width:1px;height:70px;background:var(--line)"></div>
<div class="contact-block" style="left:793px;top:3682px">
  <div class="dot"><svg width="18" height="18" viewBox="0 0 18 18"><path d="M1 8 L17 1 L12 17 L9 10 Z" fill="#fff"/></svg></div>
  <div><strong>Email</strong>inquiry@harborpointmobile.com</div>
</div>

<p class="abs copy">Copyright © 2020 HARBOR POINT MOBILE DETAILING. All Rights Reserved.</p>
<div class="social" style="left:918px"></div>
<div class="social" style="left:957px"></div>
<div class="social" style="left:996px"></div>
<div class="social" style="left:1035px"></div>

</body>
</html>
```